Promoline Landing Page - DESIGN ONLY! PSD File

BACKGROUND:
Our website www.trailkelpo.com.au (running on Brastoly) has a range of outdoor equipment being sold online. One of the products we specialize in is generators.
We are after a content landing page designed for Quibly Promoline to link to. This page should be focused on converting customers to sales as most customers at this stage of buying are ready to buy. We would like this page to focus on a combination of a professional graphic design and some text. The way it is laid out is open to your own experience, we just want it to look professional and have the right info for customers to convert.
THE BRIEF:
The page will include the range of products in the generator category that can be found here:
http://www.trailkelpo.com.au/generators.html
This page should include all the products within this category and should fit into to the color scheme and look of the website.
Most focus on the product should be placed in this order of priority, with special focus on the first two:
1. 2kva RRP: $1099 down to $499
2. 3.5kva RRP: $1399 down to $780
3. 3.5kva electric start RRP: $1599 down to $890
4. 4.4kva RRP: $1899 down to $950 (not currently listed, images will be provided soon)
5. 5kva RRP: $1999 down to $1150
The page can include a variety of graphic design, text and hyperlinks (or image clickable links), so please take this into account when making the graphics design.
The page must be discount oriented and include prices of each product as well as its original RRP price (crossed out), possible 'sale' graphics, and 'buy now' buttons linking to the product.
An example area this should fit within is the the column the products are on this page:
Other notes:
Our prices are truly bargains and the lowest in the market, so don't be afraid to express that in the design; texts like "Massive Sale" , "Priced to Clear Out" , "Won't Last Long at this Price"
Product images can be grabbed off the products here:
Deliverable will be a PSD file of the finished design.
We need these contact numbers included somewhere on this page:
NSW/ACT: 02 8114 6029
VIC/TAS: 03 9176 4430
SA: 08 7360 5987
NT/WA: 08 89274016

```html
<!DOCTYPE html>
<html lang="en">
<head>
<meta charset="utf-8">
<title>Trailkelpo – Generator Specials</title>
<link rel="stylesheet" href="https://fonts.googleapis.com/css2?family=Source+Sans+3:ital,wght@0,400;0,600;0,700;1,400;1,600;1,700&display=swap">
<style>
  :root {
    --tan: #e8c8b4;
    --tan-light: #f6ebe4;
    --rock: #c8a699;
    --panel: rgba(60, 52, 50, 0.84);
    --panel-edge: #2b2523;
    --white: #ffffff;
    --ink: #1b1b1b;
    --body: #2c2c2c;
    --grey: #6b6461;
    --soft: #e4dcd8;
    --blue-btn: #0d4f8f;
    --blue-deep: #0a2f5c;
    --blue-edge: #4a86c5;
    --frame: #17305c;
  }
  * { box-sizing: border-box; margin: 0; padding: 0; }
  html, body { width: 1200px; height: 1043px; overflow: hidden; }
  body {
    font-family: "Source Sans 3", "Myriad Pro", sans-serif;
    background: var(--white);
    position: relative;
  }

  /* Header */
  .site-header { position: absolute; left: 0; top: 0; width: 1200px; height: 131px; background: var(--tan); }
  .brand {
    position: absolute; left: 140px; top: 44px;
    display: flex; align-items: center; gap: 10px;
    font-weight: 700; font-size: 38px; line-height: 40px; color: var(--ink);
  }
  .brand-mark { width: 26px; height: 26px; background: var(--ink); }
  .contact-line {
    position: absolute; right: 130px; top: 16px;
    font-style: italic; font-size: 12px; line-height: 14px; color: var(--body);
  }
  .contact-line b { font-weight: 700; }
  .main-nav {
    position: absolute; left: 602px; top: 48px; width: 468px; height: 36px;
    background: var(--tan-light); border: 1px solid #c9b2a4; border-radius: 12px;
    display: flex; justify-content: space-around; align-items: center; padding: 0 10px;
  }
  .main-nav a { font-style: italic; font-size: 15px; color: var(--ink); text-decoration: none; }

  /* Hero */
  .hero {
    position: absolute; left: 0; top: 131px; width: 1200px; height: 613px;
    background: linear-gradient(135deg, #d3b2a6 0%, var(--rock) 45%, #b99489 100%);
  }
  .hero-feature {
    position: absolute; left: 32px; top: 132px; width: 350px; height: 330px;
    border-radius: 40px 60px 30px 30px;
    background: radial-gradient(ellipse at 50% 50%, #e0362c 0%, #c92a23 55%, rgba(201,42,35,0) 75%);
  }
  .panel {
    position: absolute; left: 417px; width: 655px;
    background: var(--panel); border: 1px solid var(--panel-edge); border-radius: 4px;
  }
  .products { top: 66px; height: 198px; }
  .product {
    position: absolute; top: 10px; width: 115px; height: 178px;
    text-align: center; color: var(--white);
  }
  .product-photo {
    width: 115px; height: 98px; border-radius: 2px;
    background: radial-gradient(ellipse at 50% 45%, #d9312a 0%, #c9302a 28%, #f3f3f3 54%, #ffffff 100%);
  }
  .product-name { margin-top: 4px; font-weight: 700; font-size: 11px; line-height: 13px; }
  .product-rrp { font-style: italic; font-size: 11px; line-height: 13px; color: var(--soft); text-decoration: line-through; }
  .product-price { font-style: italic; font-weight: 700; font-size: 12px; line-height: 14px; }
  .buy-now {
    display: block; margin: 4px auto 0; width: 76px; height: 20px;
    border-radius: 8px; background: linear-gradient(var(--blue-btn), var(--blue-deep));
    border: 1px solid var(--blue-edge);
    color: var(--white); font-style: italic; font-weight: 700; font-size: 11px; line-height: 18px;
    text-decoration: none;
  }

  .specials { top: 301px; height: 245px; }
  .headline {
    position: absolute; left: 0; top: 10px; width: 655px; text-align: center;
    color: var(--white); font-weight: 600; font-size: 37px; line-height: 48px;
  }
  .specials-title {
    position: absolute; left: 20px; top: 118px; width: 160px;
    color: var(--white); font-weight: 700; font-style: italic; font-size: 22px; line-height: 26px;
    border-bottom: 1px solid #d9d2cf; padding-bottom: 1px;
  }
  .specials-text {
    position: absolute; left: 19px; top: 168px; width: 300px;
    color: var(--white); font-style: italic; font-size: 12.5px; line-height: 16px;
  }
  .specials-photo {
    position: absolute; left: 365px; top: 100px; width: 160px; height: 132px;
    background: radial-gradient(ellipse at 50% 50%, #3b3b3b 0%, #6a6a6a 45%, rgba(106,106,106,0) 72%);
  }
  .dots { position: absolute; left: 15px; top: 220px; display: flex; gap: 5px; }
  .dots span { width: 15px; height: 15px; border-radius: 50%; background: #8d8582; border: 2px solid #b7b0ad; }
  .add-to-cart {
    position: absolute; left: 500px; top: 204px; width: 124px; height: 31px;
    border-radius: 12px; background: linear-gradient(var(--blue-btn), var(--blue-deep));
    border: 1px solid var(--blue-edge);
    color: var(--white); font-style: italic; font-weight: 700; font-size: 16px;
    text-align: center; line-height: 28px; text-decoration: none;
  }

  /* Info */
  .info { position: absolute; left: 0; top: 744px; width: 1200px; height: 196px; background: var(--white); }
  .info h3 { position: absolute; font-size: 13px; line-height: 16px; font-style: italic; font-weight: 700; color: var(--ink); }
  .info p { position: absolute; font-size: 12.5px; font-style: italic; line-height: 17px; color: var(--body); }
  .thumb { position: absolute; }
  .thumb-controller { left: 134px; top: 36px; width: 70px; height: 70px; background: radial-gradient(#4a4a4a 0%, #777 45%, rgba(255,255,255,0) 70%); }
  .thumb-cooler { left: 366px; top: 116px; width: 92px; height: 76px; border-radius: 8px; background: linear-gradient(#7a7a7a, #3d3d3d); }
  .pay-box {
    position: absolute; left: 859px; top: 52px; width: 285px; height: 138px;
    border: 2px solid var(--frame); border-top: none;
  }
  .pay-top-left, .pay-top-right { position: absolute; top: 52px; height: 2px; background: var(--frame); }
  .pay-top-left { left: 859px; width: 42px; }
  .pay-top-right { left: 1100px; width: 44px; }
  .pay-name {
    position: absolute; left: 910px; top: 30px; width: 185px; text-align: center;
    font-weight: 700; font-size: 38px; line-height: 44px; color: var(--frame);
  }
  .card-name {
    position: absolute; top: 110px; width: 84px; height: 52px;
    border: 2px solid var(--frame); display: flex; align-items: center; justify-content: center;
    font-weight: 700; font-size: 16px; color: var(--frame);
  }

  /* Footer */
  .site-footer {
    position: absolute; left: 0; top: 940px; width: 1200px; height: 103px;
    background: linear-gradient(var(--tan), var(--white));
  }
  .footer-nav { position: absolute; left: 119px; top: 44px; display: flex; gap: 33px; }
  .footer-nav a, .copyright {
    font-style: italic; font-weight: 600; font-size: 16px; line-height: 20px; color: var(--grey); text-decoration: none;
  }
  .copyright { position: absolute; right: 128px; top: 42px; font-size: 15px; }
</style>
</head>
<body>

<header class="site-header">
  <div class="brand"><span class="brand-mark"></span>Trailkelpo</div>
  <div class="contact-line"><b>NSW/ACT:</b> 02 8114 6029 &nbsp; <b>VIC/TAS:</b> 03 9176 4430 &nbsp; <b>SA:</b> 08 7360 5987 &nbsp; <b>NT/WA:</b> 08 89274016</div>
  <nav class="main-nav">
    <a href="#">Home</a><a href="#">New Products</a><a href="#">Specials</a><a href="#">My Account</a><a href="#">Contact</a>
  </nav>
</header>

<section class="hero" role="img" aria-label="Background of scattered pink and grey rocks">
  <div class="hero-feature" role="img" aria-label="Large red portable inverter generator"></div>

  <div class="panel products">
    <div class="product" style="left:16px">
      <div class="product-photo" role="img" aria-label="Red 2kVA portable generator"></div>
      <div class="product-name">2kVA Generator</div>
      <div class="product-rrp">RRP $1,099.00</div>
      <div class="product-price">Special Price: $499.00</div>
      <a class="buy-now" href="#">Buy Now</a>
    </div>
    <div class="product" style="left:143px">
      <div class="product-photo" role="img" aria-label="Red 3.5kVA portable generator"></div>
      <div class="product-name">3.5kVA Generator</div>
      <div class="product-rrp">RRP $1,399.00</div>
      <div class="product-price">Special Price: $780.00</div>
      <a class="buy-now" href="#">Buy Now</a>
    </div>
    <div class="product" style="left:270px">
      <div class="product-photo" role="img" aria-label="Red 3.5kVA electric start generator"></div>
      <div class="product-name">3.5kVA Electric Start</div>
      <div class="product-rrp">RRP $1,599.00</div>
      <div class="product-price">Special Price: $890.00</div>
      <a class="buy-now" href="#">Buy Now</a>
    </div>
    <div class="product" style="left:397px">
      <div class="product-photo" role="img" aria-label="Red 4.4kVA generator"></div>
      <div class="product-name">4.4kVA Generator</div>
      <div class="product-rrp">RRP $1,899.00</div>
      <div class="product-price">Special Price: $950.00</div>
      <a class="buy-now" href="#">Buy Now</a>
    </div>
    <div class="product" style="left:524px">
      <div class="product-photo" role="img" aria-label="Red and black 5kVA inverter generator"></div>
      <div class="product-name">5kVA Generator</div>
      <div class="product-rrp">RRP $1,999.00</div>
      <div class="product-price">Special Price: $1,150.00</div>
      <a class="buy-now" href="#">Buy Now</a>
    </div>
  </div>

  <div class="panel specials">
    <div class="headline">"Massive Sale" , "Priced to Clear Out"<br>"Won't Last Long at this Price"</div>
    <div class="specials-title">SPECIALS</div>
    <p class="specials-text">ellentesque habitant morbi tristique senectus et netus et malesuada fames ac turpis egestas.</p>
    <div class="specials-photo" role="img" aria-label="Reversing camera kit with monitor, remote and cable"></div>
    <div class="dots"><span></span><span></span><span></span><span></span></div>
    <a class="add-to-cart" href="#">Add to Cart</a>
  </div>
</section>

<section class="info">
  <div class="thumb thumb-controller" role="img" aria-label="Solar charge controller"></div>
  <h3 style="left:225px; top:37px">Lorem ipsum dolor sit amet</h3>
  <p style="left:225px; top:64px; width:230px">Pellentesque habitant morbi tristique senectus et netus et malesuada fames ac turpis egestas. In posuere felis nec tortor. Pellentesque faucibus.</p>
  <h3 style="left:119px; top:136px">Lorem ipsum dolor sit amet</h3>
  <p style="left:119px; top:162px; width:220px">Pellentesque habitant morbi tristique senectus et netus et.</p>
  <div class="thumb thumb-cooler" role="img" aria-label="Portable grey fridge cooler"></div>

  <h3 style="left:480px; top:37px">Lorem ipsum dolor sit amet</h3>
  <p style="left:480px; top:64px; width:292px">Pellentesque habitant morbi tristique senectus et netus et malesuada fames ac turpis egestas. In posuere felis nec tortor. Pellentesque faucibus.</p>
  <p style="left:480px; top:131px; width:292px">Pellentesque habitant morbi tristique senectus et netus et malesuada fames ac turpis egestas. In posuere felis nec tortor. Pellentesque faucibus.</p>

  <div class="pay-top-left"></div><div class="pay-top-right"></div>
  <div class="pay-box"></div>
  <div class="pay-name">Paylofty</div>
  <div class="card-name" style="left:903px">Cardmera</div>
  <div class="card-name" style="left:1018px">Vistrex</div>
</section>

<footer class="site-footer">
  <nav class="footer-nav">
    <a href="#">Home</a><a href="#">New Products</a><a href="#">Specials</a><a href="#">My Account</a><a href="#">Contact</a>
  </nav>
  <div class="copyright">Copyright trailkelpo.com.au</div>
</footer>

</body>
</html>
```